Business Card for Tutoring Company

We need a logo/symbol for an education company, along with an attractive business card. The logo should resemble both a pi symbol and the letter T.

Dear Designers,

I am narrowing down what I am looking for. 
I want the front of the card to be primarily white, with the company name "Maple Grove Learning" positioned towards the center.  The first letter, 'T' in 'Maple' will be modified so that it resembles a Pi symbol.
My personal information will be at the bottom.  If you think it fits, the website can be strewn across the top.

As for the back of the card, it will be primarily blue.  Toward the center will be the same T/pi shape engraved into a circular disk/button/emblem shape with some border.  It should be noted that I do like shiny blue, like the blue face of a Vantor.  Underneath the logo will be white text that reads, "Building Curious Learners and Bold Thinkers."  At the very bottom of the card in smaller white font, the website "MapleGroveLearning.com" is written.

For more clarification, see my recent attachment.

Thank you.

Winston

Industry/Entity Type

Education

Logo styles of interest
Pictorial/Combination Logo
Requirements
Must have
• LOGO:
The logo is a solid blue circle with a symbol cutout from it. The cut out should closely resemble π and be the color white.

CARD:
The front has the logo in the top left corner, with "MAPLE GROVE LEARNING" written out beside it, spanning the width of the card. " At the bottom, personal information can be placed: Name, Title, Phone, Email.
The back has the the logo centered and enlarged. The website is printed "MapleGroveLearning.com
Nice to have
• LOGO:
It would be nice if the logo/pi symbol could be used as a letter T when spelling MGL or Maple Grove Learning.

CARD:
The enlarged logo on the back of the card can be enhanced (i.e. the blue is not solid blue but shiny, like the metallic blue face of a vantor) It would also be nice if the logo had a cool background (i.e. instead of the cutout of the pi-shape being white, it could be outerspace or something. Also, a motto "Making Independent Learner and Thinkers" printed under "MapleGroveLearning.com" would be nice, if it fits.

```html
<!DOCTYPE html>
<html lang="en">
<head>
<meta charset="utf-8">
<title>Maple Grove Learning – Business Card</title>
<link rel="stylesheet" href="https://fonts.googleapis.com/css2?family=Open+Sans:wght@600;700&family=Crimson+Text:ital,wght@0,400;1,400&display=swap">
<style>
  :root {
    --canvas-bg: #e9e9ec;
    --brand-blue: #2d2f95;
    --band-deep: #1f2c9c;
    --band-mid: #3f5cc4;
    --band-light: #8fa3e4;
    --card-white: #ffffff;
    --text-white: #ffffff;
    --text-soft: #c9cdf0;
    --emblem-ring: #e8ebf7;
    --emblem-fill: #1d2466;
  }
  * { box-sizing: border-box; margin: 0; padding: 0; }
  html, body { width: 1200px; height: 873px; overflow: hidden; }
  body {
    background: var(--canvas-bg);
    display: flex;
    align-items: center;
    justify-content: center;
    gap: 60px;
  }
  .card {
    position: relative;
    width: 520px;
    height: 297px;
    border-radius: 4px;
    box-shadow: 0 8px 24px rgba(0,0,0,0.18);
    overflow: hidden;
  }

  /* Front */
  .card--front { background: var(--card-white); }
  .front__brand {
    position: absolute;
    top: 62px;
    left: 0;
    right: 0;
    display: flex;
    align-items: center;
    justify-content: center;
    gap: 14px;
  }
  .brand__dot {
    width: 44px; height: 44px;
    border-radius: 50%;
    background: var(--brand-blue);
  }
  .brand__name {
    font-family: "Open Sans", sans-serif;
    font-weight: 700;
    font-size: 31px;
    letter-spacing: 0.5px;
    color: var(--brand-blue);
  }
  .front__band {
    position: absolute;
    left: 0; right: 0; bottom: 34px;
    height: 86px;
    background: linear-gradient(90deg,
      var(--card-white) 0%,
      var(--band-deep) 7%,
      var(--band-mid) 30%,
      var(--band-light) 52%,
      var(--band-mid) 75%,
      var(--band-deep) 93%,
      var(--card-white) 100%);
    display: flex;
    justify-content: space-between;
    align-items: center;
    padding: 0 52px;
    font-family: "Crimson Text", serif;
    color: var(--text-white);
  }
  .contact__name { font-size: 24px; line-height: 1.15; }
  .contact__title { font-size: 22px; font-style: italic; line-height: 1.15; }
  .contact__details { text-align: right; font-size: 22px; line-height: 1.25; }

  /* Back */
  .card--back {
    background: var(--brand-blue);
    display: flex;
    flex-direction: column;
    align-items: center;
    color: var(--text-white);
  }
  .back__emblem {
    margin-top: 40px;
    width: 96px; height: 96px;
    border-radius: 50%;
    background: var(--emblem-fill);
    border: 4px solid var(--emblem-ring);
  }
  .back__tagline {
    margin-top: 30px;
    font-family: "Open Sans", sans-serif;
    font-weight: 700;
    font-size: 19px;
  }
  .back__website {
    margin-top: 30px;
    font-family: "Crimson Text", serif;
    font-size: 17px;
    color: var(--text-soft);
  }
</style>
</head>
<body>
  <section class="card card--front">
    <div class="front__brand">
      <span class="brand__dot"></span>
      <span class="brand__name">MAPLE GROVE LEARNING</span>
    </div>
    <div class="front__band">
      <div class="contact__person">
        <p class="contact__name">Clara Bennett</p>
        <p class="contact__title">Head Tutor</p>
      </div>
      <div class="contact__details">
        <p class="contact__phone">404.555.0187</p>
        <p class="contact__email">clara.bennett@mgl.com</p>
      </div>
    </div>
  </section>

  <section class="card card--back">
    <div class="back__emblem"></div>
    <p class="back__tagline">Building Curious Learners and Bold Thinkers</p>
    <p class="back__website">MapleGroveLearning.com</p>
  </section>
</body>
</html>
```